2026 Company Line Card

We would like to redesign our current company line card. We send this printed flyer to prospective customers to introduce our company, the brands we represent, and our competitive advantages. Our website is www.valvorimsupply.com, and our phone number is (800) 312-4470. We're a specialty supplier for plumbing material, specifically water and life safety products. Our customers are mostly male, blue-collar contractors, ages 40-60. I have included a pdf of our current flyer and our high-resolution transparent logo. We would also like to highlight certain key points, which include:
Genuine OEM Parts
Technical Assistance from Repair Experts
Repair Information
1-2 day Delivery for the United States
Friendly & Knowledgeable Customer Service
The Largest Parts Inventory In The Nation
Testing Equipment
Full Service Gauge Calibration and Repair

```html
<!DOCTYPE html>
<html lang="en">
<head>
<meta charset="utf-8">
<title>Valvorim Supply Co. — 2026 Line Card</title>
<link href="https://fonts.googleapis.com/css2?family=Barlow+Condensed:ital,wght@1,700&family=Montserrat:wght@700&family=Oswald:wght@300;600&family=Source+Sans+3:wght@600;700&display=swap" rel="stylesheet">
<style>
  :root{
    --blue:#1252a8;
    --navy:#0b3877;
    --sky:#5b8fd0;
    --red:#e6262b;
    --paper:#f3f4f7;
    --mist:#dfe2e8;
    --ink:#1c2438;
    --night:#141414;
    --white:#ffffff;
  }
  *{margin:0;padding:0;box-sizing:border-box}
  html,body{width:999px;height:1200px;overflow:hidden;background:var(--paper)}
  .card{position:relative;width:999px;height:1200px;overflow:hidden;background:var(--paper)}
  .backdrop{position:absolute;inset:0}
  .brand{position:absolute;left:40px;top:38px;display:flex;align-items:center;gap:14px}
  .brand-dot{width:40px;height:40px;border-radius:50%;background:var(--red)}
  .brand-name{font-family:"Source Sans 3",sans-serif;font-weight:600;font-size:34px;color:var(--blue);letter-spacing:.2px}
  .tagline{position:absolute;left:62px;top:224px;font-family:"Montserrat",sans-serif;font-weight:700;font-size:21px;color:var(--white)}
  .checklist{position:absolute;left:48px;top:282px;list-style:none}
  .checklist li{display:flex;align-items:center;gap:8px;height:47px;font-family:"Barlow Condensed",sans-serif;font-style:italic;font-weight:700;font-size:40px;color:var(--white)}
  .checklist svg{width:30px;height:30px;flex:none}
  .feature{position:absolute;width:120px;text-align:center;font-family:"Oswald",sans-serif;font-weight:300;font-size:18px;line-height:22px;color:var(--white)}
  .section-title{position:absolute;left:722px;top:578px;font-family:"Oswald",sans-serif;font-weight:600;font-size:42px;color:var(--navy)}
  .section-title span{color:var(--blue)}
  .partners{position:absolute;left:51px;top:982px;width:892px;height:128px;background:var(--white);border:2px solid var(--mist);border-radius:28px}
  .partner{position:absolute;transform:translate(-50%,-50%);display:flex;align-items:center;gap:5px;white-space:nowrap;font-family:"Source Sans 3",sans-serif;font-weight:700;font-size:17px}
  .partner i{display:block;width:11px;height:11px}
  .contact{position:absolute;top:1126px;display:flex;align-items:center;gap:12px;font-family:"Montserrat",sans-serif;font-weight:700;font-size:23px;color:var(--white)}
  .contact svg{width:48px;height:48px}
</style>
</head>
<body>
<main class="card">
  <svg class="backdrop" width="999" height="1200" viewBox="0 0 999 1200">
    <defs>
      <linearGradient id="valveTone" x1="0" y1="0" x2="1" y2="1">
        <stop offset="0" stop-color="#2656a6"/>
        <stop offset=".55" stop-color="#d42a26"/>
        <stop offset="1" stop-color="#c9cdd4"/>
      </linearGradient>
      <linearGradient id="gearTone" x1="0" y1="0" x2="1" y2="0">
        <stop offset="0" stop-color="#cfd6dd"/>
        <stop offset="1" stop-color="#e9ebee"/>
      </linearGradient>
    </defs>
    <polygon points="0,280 999,22 999,945 0,730" fill="var(--blue)"/>
    <polygon points="365,142 999,-4 999,10 395,142" fill="var(--sky)"/>
    <polygon points="730,64 999,0 999,28 800,64" fill="var(--red)"/>
    <polygon points="470,150 999,24 999,445 480,577 440,560" fill="url(#valveTone)" role="img" aria-label="Photo of red backflow preventer valve assembly on concrete supports"/>
    <polygon points="480,577 999,445 999,760" fill="var(--mist)"/>
    <polygon points="0,462 999,760 999,945 0,730" fill="var(--navy)"/>
    <polygon points="0,652 80,634 80,638 0,656" fill="var(--white)" opacity=".8"/>
    <polygon points="0,674 120,644 120,648 0,678" fill="var(--white)" opacity=".8"/>
    <polygon points="0,221 545,221 545,263 0,263" fill="var(--red)"/>
    <rect x="0" y="707" width="219" height="275" rx="6" fill="url(#gearTone)" role="img" aria-label="Photo of a hand holding a digital backflow test kit with hoses"/>
    <rect x="244" y="834" width="573" height="134" rx="8" fill="url(#gearTone)" role="img" aria-label="Photos of a test kit case, check valve parts, springs, seals and a bronze ball valve"/>
    <rect x="0" y="1082" width="999" height="118" fill="var(--night)"/>

    <g fill="var(--red)">
      <circle cx="94" cy="490" r="38"/><circle cx="211" cy="526" r="38"/>
      <circle cx="328" cy="563" r="38"/><circle cx="443" cy="598" r="38"/>
      <circle cx="561" cy="634" r="38"/><circle cx="684" cy="670" r="38"/>
      <circle cx="801" cy="706" r="38"/><circle cx="919" cy="742" r="38"/>
    </g>
    <g fill="none" stroke="var(--white)" stroke-width="2.4" stroke-linecap="round" stroke-linejoin="round">
      <path d="M94 470 l18 6 v10 c0 12 -8 20 -18 24 c-10 -4 -18 -12 -18 -24 v-10 z"/>
      <path d="M86 490 l6 6 l11 -12"/>
      <circle cx="211" cy="518" r="10"/><path d="M193 538 h12 l8 -4 h8"/>
      <rect x="312" y="548" width="32" height="22" rx="2"/><path d="M328 570 v6 M320 577 h16"/>
      <path d="M424 590 h22 v18 h-22 z M446 596 h8 l6 7 v5 h-14"/><circle cx="432" cy="610" r="3"/><circle cx="452" cy="610" r="3"/>
      <circle cx="561" cy="626" r="8"/><path d="M547 650 c2 -10 8 -14 14 -14 s12 4 14 14 M551 626 c0 -8 5 -12 10 -12 s10 4 10 12"/>
      <rect x="672" y="654" width="22" height="30" rx="2"/><path d="M677 662 h12 M677 669 h12 M677 676 h8"/>
      <circle cx="801" cy="706" r="14"/><path d="M794 706 l5 5 l9 -10"/>
      <circle cx="919" cy="742" r="9"/><circle cx="919" cy="742" r="17" stroke-dasharray="5 4"/>
    </g>
  </svg>

  <div class="brand"><span class="brand-dot"></span><span class="brand-name">Valvorim Supply Co.</span></div>

  <p class="tagline">The Nation’s Leading Source for</p>
  <ul class="checklist">
    <li><svg viewBox="0 0 30 30"><circle cx="15" cy="15" r="12" fill="none" stroke="#fff" stroke-width="3"/><path d="M9 15 l5 5 l12 -14" fill="none" stroke="#fff" stroke-width="3.2" stroke-linecap="round"/></svg>Genuine OEM Parts</li>
    <li><svg viewBox="0 0 30 30"><circle cx="15" cy="15" r="12" fill="none" stroke="#fff" stroke-width="3"/><path d="M9 15 l5 5 l12 -14" fill="none" stroke="#fff" stroke-width="3.2" stroke-linecap="round"/></svg>Repair Information</li>
    <li><svg viewBox="0 0 30 30"><circle cx="15" cy="15" r="12" fill="none" stroke="#fff" stroke-width="3"/><path d="M9 15 l5 5 l12 -14" fill="none" stroke="#fff" stroke-width="3.2" stroke-linecap="round"/></svg>Technical Assistance</li>
  </ul>

  <p class="feature" style="left:34px;top:538px">Genuine<br>OEM Parts</p>
  <p class="feature" style="left:151px;top:574px">Technical<br>Assistance from<br>Repair Experts</p>
  <p class="feature" style="left:268px;top:611px">Repair<br>Information</p>
  <p class="feature" style="left:383px;top:646px">1-2 day<br>Delivery for<br>the United<br>States</p>
  <p class="feature" style="left:501px;top:682px">Friendly &amp;<br>Knowledgeable<br>Customer<br>Service</p>
  <p class="feature" style="left:624px;top:718px">The Largest<br>Parts Inventory<br>In The Nation</p>
  <p class="feature" style="left:741px;top:754px">Testing<br>Equipment</p>
  <p class="feature" style="left:859px;top:790px">Full Service<br>Gauge<br>Calibration<br>and Repair</p>

  <h2 class="section-title"><span>Our</span> Service</h2>

  <section class="partners" aria-label="Brands we carry">
    <span class="partner" style="left:103px;top:41px;color:var(--red)"><i style="background:var(--red)"></i>Kestrel</span>
    <span class="partner" style="left:222px;top:41px;color:var(--ink)">Norhaven</span>
    <span class="partner" style="left:323px;top:41px;color:#a8781a">Brightwell Valves</span>
    <span class="partner" style="left:450px;top:41px;color:var(--navy)">Tarsa</span>
    <span class="partner" style="left:573px;top:41px;color:var(--navy)">Ostrand</span>
    <span class="partner" style="left:663px;top:41px;color:var(--navy)"><i style="background:var(--navy)"></i>Dunmore</span>
    <span class="partner" style="left:782px;top:41px;color:#7a3a2c">Ridgefold</span>
    <span class="partner" style="left:103px;top:88px;color:var(--ink)">Halvec</span>
    <span class="partner" style="left:222px;top:88px;color:var(--navy)">Pellcor</span>
    <span class="partner" style="left:323px;top:88px;color:var(--red)">Thermshell</span>
    <span class="partner" style="left:450px;top:88px;color:#3aa04a">Corvid Gauge</span>
    <span class="partner" style="left:573px;top:88px;color:var(--blue)">Guardlid</span>
    <span class="partner" style="left:663px;top:88px;color:var(--navy)">Brennick</span>
    <span class="partner" style="left:782px;top:88px;color:var(--blue)">Ashgrove</span>
  </section>

  <div class="contact" style="left:164px">
    <svg viewBox="0 0 48 48"><circle cx="24" cy="24" r="24" fill="var(--blue)"/><path d="M17 12 l5 -1 l3 8 l-4 3 c2 4 4 6 7 7 l3 -4 l8 3 l-1 5 c-11 1 -22 -10 -21 -21 z" fill="#fff"/></svg>
    <span>(800) 312-4470</span>
  </div>
  <div class="contact" style="left:460px">
    <svg viewBox="0 0 48 48"><circle cx="24" cy="24" r="24" fill="var(--blue)"/><g fill="none" stroke="#fff" stroke-width="2"><circle cx="24" cy="24" r="13"/><ellipse cx="24" cy="24" rx="6" ry="13"/><path d="M11 24 h26 M13 17 h22 M13 31 h22"/></g></svg>
    <span>www.valvorimsupply.com</span>
  </div>
</main>
</body>
</html>
```